Research, Writing and Editing business needs a Business Card Design

I need a business card design for a new company based in Melbourne called The Amber Advisory Collective. We provide research, writing and editing services. The company logo is attached, but I am open to your creative designs for business cards with the logo. As you will note, there are two potential logos. Feel free to use either of the logos.

The overall look I am hoping for is sleek, sophisticated, feminine and elegant.

Thanks in advance for your efforts.

Target Market(s)

Business professionals, academics and students

Industry/Entity Type

Business

Font styles to use
Serif
Script

Colors

Designer to choose colors to be used in the design.

Requirements
Must have
• The Amber Advisory Collective
Dr Nola Fenwick

M: 0482 593 247
E: nola@theamberadvisorycollective.com.au
W: theamberadvisorycollective.com.au
Nice to have
• Research | Writing | Editing

```html
<!DOCTYPE html>
<html lang="en">
<head>
<meta charset="utf-8">
<title>The Amber Advisory Collective – Business Card</title>
<link rel="stylesheet" href="https://fonts.googleapis.com/css2?family=Alike&family=Open+Sans:wght@400&display=swap">
<style>
  :root {
    --page-bg: #ffffff;
    --label-ink: #111111;
    --card-light: #ab95c9;
    --card-mid: #9a80bf;
    --card-edge: #7447a5;
    --card-ink: #1a1420;
    --rule-ink: #3a2d48;
  }
  html, body {
    margin: 0;
    padding: 0;
    width: 1200px;
    height: 900px;
    overflow: hidden;
    background: var(--page-bg);
  }
  .sheet {
    position: relative;
    width: 1200px;
    height: 900px;
  }
  .dimension-label,
  .side-label {
    position: absolute;
    font-family: "Open Sans", Arial, sans-serif;
    color: var(--label-ink);
    line-height: 1;
    margin: 0;
  }
  .dimension-label { font-size: 36px; }
  .side-label { font-size: 44px; }
  .width-top { left: 557px; top: 8px; }
  .width-bottom { left: 584px; top: 857px; }
  .height-front { left: 1065px; top: 210px; }
  .height-back { left: 1092px; top: 650px; }
  .label-front { left: 3px; top: 184px; }
  .label-back { left: -1px; top: 596px; }

  .card {
    position: absolute;
    left: 247px;
    width: 771px;
    height: 364px;
    border-radius: 28px;
    background: radial-gradient(ellipse 62% 66% at 50% 48%, var(--card-light) 0%, var(--card-light) 45%, var(--card-mid) 78%, var(--card-edge) 100%);
    box-shadow: 1px 2px 2px rgba(0,0,0,0.35);
    color: var(--card-ink);
    font-family: "Alike", Georgia, serif;
  }
  .card-front { top: 66px; }
  .card-back { top: 479px; }

  .front-wordmark {
    position: absolute;
    left: 0;
    right: 0;
    top: 162px;
    text-align: center;
    font-size: 40px;
    letter-spacing: 0.5px;
    margin: 0;
    font-weight: 400;
  }
  .back-wordmark {
    position: absolute;
    left: 22px;
    top: 52px;
    font-size: 17px;
    margin: 0;
    font-weight: 400;
  }
  .holder-name {
    position: absolute;
    right: 70px;
    top: 114px;
    font-size: 26px;
    margin: 0;
    font-weight: 400;
    letter-spacing: 0.3px;
  }
  .name-rule {
    position: absolute;
    left: 456px;
    top: 146px;
  }
  .contact-list {
    list-style: none;
    margin: 0;
    padding: 0;
    position: absolute;
    right: 36px;
    top: 246px;
  }
  .contact-item {
    display: flex;
    justify-content: flex-end;
    align-items: center;
    gap: 18px;
    height: 29px;
  }
  .contact-phone { font-size: 19px; }
  .contact-email { font-size: 14px; }
  .contact-web { font-size: 13px; }
  .contact-icon { width: 26px; height: 22px; flex: none; }
</style>
</head>
<body>
<main class="sheet">
  <p class="dimension-label width-top">9 cm</p>
  <p class="side-label label-front">FRONT</p>
  <p class="dimension-label height-front">5 cm</p>

  <section class="card card-front" aria-label="Card front">
    <h1 class="front-wordmark">The Amber Advisory Collective</h1>
  </section>

  <p class="side-label label-back">BACK</p>
  <p class="dimension-label height-back">5 cm</p>

  <section class="card card-back" aria-label="Card back">
    <p class="back-wordmark">The Amber Advisory Collective</p>

    <h2 class="holder-name">Dr Nola Fenwick</h2>
    <svg class="name-rule" width="246" height="10" viewBox="0 0 246 10" aria-hidden="true">
      <polyline points="0,5 110,5 116,1 122,5 246,5" fill="none" stroke="var(--rule-ink)" stroke-width="1"/>
    </svg>

    <ul class="contact-list">
      <li class="contact-item contact-phone">
        <span>0482 593 247</span>
        <svg class="contact-icon" viewBox="0 0 26 22" aria-hidden="true">
          <path d="M6 3 l4 0 l2 5 l-3 2 q2 4 6 6 l2-3 l5 2 l0 4 q-1 2-4 2 q-8-1-13-8 q-2-4-1-8 z" fill="var(--card-ink)"/>
        </svg>
      </li>
      <li class="contact-item contact-email">
        <span>nola@theamberadvisorycollective.com.au</span>
        <svg class="contact-icon" viewBox="0 0 26 22" aria-hidden="true">
          <rect x="2" y="3" width="22" height="16" fill="none" stroke="var(--card-ink)" stroke-width="1.6"/>
          <polyline points="2,3 13,12 24,3" fill="none" stroke="var(--card-ink)" stroke-width="1.6"/>
        </svg>
      </li>
      <li class="contact-item contact-web">
        <span>theamberadvisorycollective.com.au</span>
        <svg class="contact-icon" viewBox="0 0 26 22" aria-hidden="true">
          <circle cx="13" cy="11" r="9" fill="none" stroke="var(--card-ink)" stroke-width="1.8"/>
          <ellipse cx="13" cy="11" rx="4" ry="9" fill="none" stroke="var(--card-ink)" stroke-width="1.4"/>
          <line x1="4" y1="11" x2="22" y2="11" stroke="var(--card-ink)" stroke-width="1.4"/>
        </svg>
      </li>
    </ul>
  </section>

  <p class="dimension-label width-bottom">9 cm</p>
</main>
</body>
</html>
```